Personal Business card and maybe logo or graphic?

I would like a card to give out like you would a business card, however I am not promoting a business, it is just for my personal details.

I have no brand and no logo to worry about.

I would like some images or a logo of some kind or a graphic so the card has some excitement about it.

I am happy if you wish to create a logo/graphic that represents my name, I have seen someone with just their initials as a graphic so for me PH, however I am happy for you to create anything you wish, it does not have to relate to me just make the card look fun and still professional.

Please use the details

Peter Hallam

Thornbury Lodge
9 Kestle Row
Moss Bank
Harbourne
Carrowshire
BH4 2QD

+44 (0)7812 460583
peter@hallampost.net
linkedin.com/in/hallampeter

looking for a mix between fun, fresh , young whilst being professional

I am new to this and am looking for you to guide me through the process please ask questions and ideas

I am just tidying up my brief as I am starting to understand more. hope it has not confused anyone
Updates

Reason: I have not had time to review or comment due to personal issues sorry

Hi,

to help would you be so kind as to use these sample details on the card

I am uk based and a few designs have us details which look different

Peter Hallam

Thornbury lodge

9 Kestle Row

Moss Bank

Harbourne

Carrowshire

BH4 2QD

+44 (0)7812 460583

peter@hallampost.net

many thanks hope that is ok and not too much trouble!

regards

Pete

My are of expertise is IT management / IT Consultancy, incase you wish to incorporate any graphics

My job was that of CIO (Chief Information Officer) or another term is Head of IT

just advising incase this gives any assistance as one designer has asked s may be useful to others

thanks                                   

just thought I have had a look and the UK size for a business card seems to be as per below

I thought I would mention as I guess the US size may be different and other countries too

I found these sizes on Quillpress but guess most companies will be similar

that said maybe you can advise me

I have no idea what quillpress is like so not sure where to get cards made, will figure that out later I guess but I assume dimensions are important for the design

thanks

 

Document Trim Size    

            Horizontal        

        85 x 55 mm           

1004 x 650 pixels           

            Vertical        

        55 x 85 mm           

650 x 1004 pixels           

        Full Bleed Size    

            Horizontal        

        88 x 58 mm           

1039 x 685 pixels           

            Vertical        

        58 x 88 mm           

685 x 1039 pixels           

 many thanks

Target Market(s)

Professional and personal contacts

Industry/Entity Type

Business

```html
<!DOCTYPE html>
<html lang="en">
<head>
<meta charset="utf-8">
<title>Peter Hallam – Personal Card</title>
<link href="https://fonts.googleapis.com/css2?family=Tinos:wght@400;700&family=Crimson+Pro:wght@400;500&family=Bodoni+Moda:wght@700&display=swap" rel="stylesheet">
<style>
  :root {
    --backdrop: #e9e6e1;
    --card-white: #ffffff;
    --ink: #111111;
    --accent-red: #e4202a;
    --band-blue: #00adef;
  }
  html, body {
    margin: 0;
    padding: 0;
    overflow: hidden;
  }
  body {
    width: 1200px;
    height: 1200px;
    background: var(--backdrop);
    position: relative;
  }
  .card {
    position: absolute;
    left: 180px;
    width: 840px;
    height: 544px;
    border-radius: 34px;
    background: var(--card-white);
    overflow: hidden;
    box-shadow: 0 6px 18px rgba(0,0,0,0.12);
  }
  .card--front { top: 36px; }
  .card--back { top: 620px; }

  .monogram {
    position: absolute;
    display: flex;
    align-items: center;
    gap: 14px;
    font-family: "Tinos", "Times New Roman", serif;
    font-weight: 700;
    color: var(--ink);
    line-height: 1;
    white-space: nowrap;
  }
  .monogram__dot {
    width: 22px;
    height: 22px;
    border-radius: 50%;
    background: var(--accent-red);
  }
  .card--front .monogram {
    left: 130px;
    top: 226px;
    font-size: 120px;
  }

  .divider {
    position: absolute;
    left: 416px;
    top: 62px;
    width: 5px;
    height: 448px;
    background: var(--ink);
  }
  .identity {
    position: absolute;
    left: 436px;
    top: 196px;
    width: 396px;
    text-align: center;
  }
  .identity__name {
    margin: 0;
    font-family: "Crimson Pro", "Times New Roman", serif;
    font-weight: 400;
    font-size: 70px;
    line-height: 1;
    letter-spacing: -1px;
    white-space: nowrap;
    color: var(--ink);
  }
  .identity__role {
    margin: 12px 0 0;
    font-family: "Crimson Pro", "Times New Roman", serif;
    font-weight: 500;
    font-size: 30px;
    white-space: nowrap;
    color: var(--accent-red);
  }

  .band {
    position: absolute;
    left: 0;
    width: 100%;
    background: var(--band-blue);
  }
  .band--top { top: 0; height: 182px; }
  .band--bottom { top: 460px; height: 84px; }

  .card--back .monogram {
    left: 50%;
    top: 104px;
    transform: translateX(-50%);
    font-size: 110px;
  }
  .address {
    position: absolute;
    left: 150px;
    top: 236px;
    margin: 0;
    font-family: "Tinos", "Times New Roman", serif;
    font-size: 37px;
    line-height: 1.04;
    color: var(--ink);
    font-style: normal;
    white-space: nowrap;
  }
  .contact {
    position: absolute;
    left: 460px;
    top: 232px;
    margin: 0;
    color: var(--ink);
    white-space: nowrap;
  }
  .contact__county,
  .contact__postcode {
    display: block;
    font-family: "Bodoni Moda", "Times New Roman", serif;
    font-weight: 700;
    letter-spacing: 4px;
  }
  .contact__county { font-size: 34px; line-height: 1.1; }
  .contact__postcode { font-size: 27px; line-height: 1.25; }
  .contact__phone {
    display: block;
    font-family: "Tinos", "Times New Roman", serif;
    font-size: 33px;
    line-height: 1.35;
  }
  .contact__email {
    display: block;
    font-family: "Tinos", "Times New Roman", serif;
    font-size: 28px;
    line-height: 1.2;
  }
  .profile-link {
    position: absolute;
    left: 0;
    top: 466px;
    width: 100%;
    text-align: center;
    font-family: "Tinos", "Times New Roman", serif;
    font-size: 30px;
    letter-spacing: 1.5px;
    color: var(--accent-red);
  }
</style>
</head>
<body>

  <section class="card card--front" aria-label="Card front">
    <div class="monogram"><span>PH</span><span class="monogram__dot"></span></div>
    <div class="divider"></div>
    <div class="identity">
      <h1 class="identity__name">Peter Hallam</h1>
      <p class="identity__role">Chief Information Officer</p>
    </div>
  </section>

  <section class="card card--back" aria-label="Card back">
    <div class="band band--top"></div>
    <div class="band band--bottom"></div>
    <div class="monogram"><span>PH</span><span class="monogram__dot"></span></div>
    <address class="address">
      Thornbury lodge<br>
      9 Kestle Row<br>
      Moss Bank<br>
      Harbourne
    </address>
    <p class="contact">
      <span class="contact__county">Carrowshire</span>
      <span class="contact__postcode">BH4 2QD</span>
      <span class="contact__phone">+44 (0)7812 460583</span>
      <span class="contact__email">peter@hallampost.net</span>
    </p>
    <div class="profile-link">profilehub.net/in/hallampeter</div>
  </section>

</body>
</html>
```